Hosted PBX VoIP Web Site Redesign WordPress Template

We offer hosted 'in the cloud' telephone services. Our current site is http://www.brambleviewtelco.com and the site needs a major work-over. The site MUST BE be completed in WordPress as a template design.
I want this new site to have a warm look and feel giving the impression that we give the best customer service for small to medium businesses. The target business customer is small business with 5 to 50 employees with remote working employees who need to stay in communications with other staff.
Differentiation from our competitors is what we are looking for. We have been selling hosted pbx services for more than 7 years, we own our data center and have been in the data center business since 2000. Here are some examples of what I would like to have as a new web site:
Other hosted PBX companies:
http://www.quorvelle.com/
http://www.dunmira.com/
http://www.trevanixo.com/
http://www.holvex.com/
http://www.bluntorrax.com/
Not Hosted PBX companies, but sites I like are:
http://www.kelmoraps.com/
http://www.zuvantel.com/
http://www.grindlepost.com/
I don't want a copy-cat web site and will invest in good graphics and original photography and graphics as needed.
Rona Pelham
http://www.brambleviewweb.com
Updates
Here are some ideas I have look at. I want a very clean Word Press web site like these:
Other hosted PBX companies that we can get some graphic ideas from and good content.
http://www.quorvelle.com/
http://www.dunmira.com/
http://www.holvex.com/
http://www.bluntorrax.com/
http://www.vostel.com/
http://www.quillbranch.com/
http://www.kelmoraps.com/
http://www.zuvantel.com/ - I like this clean design
http://www.grindlepost.com/
I have engaged Ostrava7.4 Media Group to make a video similar to this one to embed on our new home page, They did a good job with the copy and graphics on the http://www.Fernquay.com video. This is the video I want them to emulate http://www.enterprise.holbrine.com/content/mixedmedia/CallWeave_H264.mp4 Watch this video. It tells what we do but on a smaller scale. We don't have the budget Holbrine has to do what they did.
When needed I will engage http://www.wordmelder.com to write come fresh new content work our new web site. That is why it's important that it be a good WordPress template that I can add news articles to for good SEO.
Rona
Target Market(s)
small business owners, business with tele or remote workers
Industry/Entity Type
Small Business
Requirements
Must have
- clean look and feel, easy to read. I might a video that explains our service. Here's what we do. Watch this video at http://www.enterprise.holbrine.com/content/mixedmedia/CallWeave_H264.mp4 to better understand the services we offer.
Nice to have
- Our logo can be redesigned as needed to fix the new look and feel. Brambleview Telco Line is our name but we are willing to change our name to just Brambleview Telco if the name fits the new look and feel.

```html
<!DOCTYPE html>
<html lang="en">
<head>
<meta charset="utf-8">
<title>Brambleview Telco — Hosted Phone Service</title>
<link href="https://fonts.googleapis.com/css2?family=Open+Sans:wght@400;600&family=Merriweather:wght@300;400&display=swap" rel="stylesheet">
<style>
:root{
  --sky:#2fb7e6;
  --sky-light:#5fd0f2;
  --page-bg:#a9bccb;
  --page-bg-dark:#95aabb;
  --card:#ffffff;
  --hero-top:#4c8fc1;
  --hero-bottom:#1f5d92;
  --accent-yellow:#f2ee3a;
  --ink:#2f2f2f;
  --heading:#3b5566;
  --button-top:#2f9de4;
  --button-bottom:#0f6db8;
  --placeholder:#3c3c3c;
  --footer:#1e1e1e;
  --footer-text:#e8e8e8;
  --logo-blue:#1b5fb0;
}
*{margin:0;padding:0;box-sizing:border-box}
html,body{width:693px;height:1200px;overflow:hidden;background:var(--footer)}
.stage{position:relative;width:800px;height:1385px;transform:scale(.86625);transform-origin:0 0;font-family:"Merriweather",Georgia,serif;color:var(--ink);
  background:
    linear-gradient(to bottom,#eef1f3 0,#dfe4e8 47px,transparent 47px),
    linear-gradient(to bottom,var(--sky) 47px,var(--sky-light) 110px,#7fc6df 150px,var(--page-bg) 150px,var(--page-bg-dark) 1125px,var(--footer) 1125px);}
.abs{position:absolute}
.brand{left:70px;top:18px;font-family:"Open Sans",sans-serif;font-weight:600;font-size:19px;color:var(--logo-blue);display:flex;align-items:center;gap:6px}
.brand-dot{width:8px;height:8px;border-radius:50%;background:var(--logo-blue)}
.card{background:var(--card);border-radius:4px;box-shadow:0 1px 4px rgba(0,0,0,.25)}
.nav{left:53px;top:73px;width:697px;height:30px;border-radius:4px 4px 0 0;background:linear-gradient(#f4f5f6,#c9cfd4);border-bottom:3px solid #8fc9e3;display:flex;padding-left:155px;font-family:"Open Sans",sans-serif}
.nav-item{display:flex;align-items:center;justify-content:space-between;padding-right:8px}
.nav-label{line-height:1}
.nav-label b{display:block;font-weight:400;font-size:14px;color:#2a3a48}
.nav-label small{display:block;font-size:6.5px;letter-spacing:1px;font-weight:600;color:#2a3a48;margin-top:1px}
.nav-dot{width:9px;height:9px;border-radius:50%;background:#6aa6cc}
.hero{left:71px;top:128px;width:659px;height:280px;border-radius:6px;background:linear-gradient(160deg,var(--hero-top),var(--hero-bottom));border:1px solid #1b4e7a}
.hero h1{position:absolute;left:40px;top:30px;font-family:"Open Sans",sans-serif;font-weight:400;font-size:36px;color:#fff;letter-spacing:-1px}
.hero h2{position:absolute;left:40px;top:72px;font-family:"Open Sans",sans-serif;font-weight:400;font-size:19px;color:var(--accent-yellow);letter-spacing:-.5px}
.hero p{position:absolute;left:43px;top:108px;width:312px;font-size:11px;line-height:18px;color:#fff;font-weight:300}
.hero p em{font-style:normal;color:var(--accent-yellow)}
.hero-btn{position:absolute;left:161px;top:224px;width:155px;height:32px;border-radius:4px;background:linear-gradient(var(--button-top),var(--button-bottom));border:1px solid #0b4f87;color:#fff;font-family:"Open Sans",sans-serif;font-size:13px;letter-spacing:1px;display:flex;align-items:center;justify-content:center}
.hero-art{position:absolute;left:375px;top:45px;width:240px;height:200px;border-radius:8px;background:radial-gradient(circle at 45% 45%,#dbe7f1,#3f8fd6 60%,rgba(31,93,146,0) 75%)}
.tagline{left:71px;top:421px;width:659px;height:87px;border-radius:6px;border:1px solid #4a7aa0;background:linear-gradient(#fff,#d5d5d5);display:flex;align-items:center;padding-left:39px;font-family:"Open Sans",sans-serif;font-size:15.5px;letter-spacing:-.3px;white-space:nowrap;color:#3f3f3f}
.main-menu{left:70px;top:547px}
.main-menu h3{font-family:"Open Sans",sans-serif;font-weight:400;font-size:17px;color:#1f1f1f;margin-bottom:6px}
.main-menu li{list-style:none;font-family:"Open Sans",sans-serif;font-size:13px;letter-spacing:.8px;line-height:17.6px;padding-left:18px;position:relative;color:#222}
.main-menu li::before{content:"›";position:absolute;left:0;top:-1px}
.feature{width:142px;height:125px}
.feature-icon{float:left;width:48px;height:47px;margin:0 2px 0 0}
.feature h4{font-family:"Open Sans",sans-serif;font-weight:400;font-size:18px;line-height:24px;color:var(--heading);letter-spacing:.4px;white-space:nowrap}
.feature p{font-size:7.8px;line-height:13px;margin-top:1px}
.btn{position:absolute;border-radius:2px;background:linear-gradient(var(--button-top),var(--button-bottom));color:#fff;font-family:"Open Sans",sans-serif;font-size:8px;display:flex;align-items:center;justify-content:center;letter-spacing:.5px}
.feature .btn{left:4px;top:104px;width:55px;height:17px}
.session{left:72px;top:835px;width:175px;height:170px}
.session h3{font-family:"Open Sans",sans-serif;font-weight:400;font-size:16.5px;color:var(--heading);letter-spacing:.8px}
.session p{font-size:8.4px;line-height:12.6px;margin-top:8px}
.session .btn{left:0;top:146px;width:78px;height:17px;font-size:9px}
.shot{width:211px}
.shot-img{height:105px;background:var(--placeholder)}
.shot-cap{font-size:8.6px;margin-top:10px;padding-bottom:6px;border-bottom:1px solid #555}
.foot-col{top:1190px;color:var(--footer-text);font-size:9px}
.foot-col h5{font-family:"Open Sans",sans-serif;font-weight:400;font-size:14px;line-height:14px;margin-bottom:9px;color:#f3f3f3}
.pages li{list-style:none;width:110px;padding:4px 0;border-bottom:1px solid #333;font-size:10px}
.bullets li{list-style:none;position:relative;padding-left:12px;line-height:14px}
.bullets li::before{content:"›";position:absolute;left:2px;color:#9fbf3a}
.divider{top:1190px;width:1px;height:120px;background:#333}
.foot-brand{right:71px;top:1338px;text-align:right;color:#fff;font-family:"Open Sans",sans-serif}
.foot-brand strong{display:block;font-weight:400;font-size:17px;line-height:18px}
.foot-brand span{font-size:8px}
</style>
</head>
<body>
<div class="stage">
  <div class="abs brand"><span class="brand-dot"></span>Brambleview Telco</div>

  <div class="abs card" style="left:53px;top:73px;width:697px;height:448px"></div>
  <nav class="abs nav">
    <div class="nav-item" style="width:83px"><div class="nav-label"><b>home</b><small>START HERE</small></div><span class="nav-dot"></span></div>
    <div class="nav-item" style="width:87px"><div class="nav-label"><b>services</b><small>FEATURES</small></div><span class="nav-dot"></span></div>
    <div class="nav-item" style="width:82px"><div class="nav-label"><b>partners</b><small>OUR GROUP</small></div><span class="nav-dot"></span></div>
    <div class="nav-item" style="width:100px"><div class="nav-label"><b>equipment</b><small>TECHNOLOGY</small></div><span class="nav-dot"></span></div>
    <div class="nav-item" style="width:86px"><div class="nav-label"><b>about us</b><small>OUR VISION</small></div><span class="nav-dot"></span></div>
    <div class="nav-item" style="width:100px"><div class="nav-label"><b>contact</b><small>TALK WITH US</small></div><span class="nav-dot"></span></div>
  </nav>

  <section class="abs hero">
    <h1>Introducing...</h1>
    <h2>The Brambleview Telco Line Suite</h2>
    <p>Vivamus feugiat hendrerit diam non posuere. Nunc ligula libero, suscipit eu fermentum sit amet, adipiscing ut ipsum. <em>Sed venenatis lacinia tellus eu malesuada.</em> Sed cursus feugiat massa vitae auctor. Morbi interdum vestibulum eros, at rutrum enim ullamcorper in. <em>Vestibulum lectus leo</em>, rhoncus at rhoncus sit amet, semper id massa.</p>
    <div class="hero-btn">Learn more here</div>
    <div class="hero-art" role="img" aria-label="Illustration of an email envelope, a blue telephone handset and a settings gear"></div>
  </section>

  <div class="abs tagline">Incredibly advanced business phone service right over your Internet connection.</div>

  <div class="abs card" style="left:53px;top:535px;width:697px;height:637px"></div>

  <div class="abs main-menu">
    <h3>Main Menu</h3>
    <ul><li>Home</li><li>Services</li><li>Partners</li><li>Equipment</li><li>Gallery</li><li>About Us</li><li>Contact</li></ul>
  </div>

  <svg width="0" height="0" style="position:absolute">
    <defs>
      <symbol id="magnifier" viewBox="0 0 48 50">
        <line x1="30" y1="30" x2="44" y2="46" stroke="#3a3a3a" stroke-width="6" stroke-linecap="round"/>
        <circle cx="20" cy="20" r="16" fill="#d7e3ea" stroke="#9aa5ad" stroke-width="4"/>
        <ellipse cx="15" cy="14" rx="7" ry="4" fill="#fff" opacity=".8"/>
      </symbol>
    </defs>
  </svg>

  <div class="abs feature" style="left:236px;top:552px"><svg class="feature-icon" viewBox="0 0 48 50"><use href="#magnifier"/></svg><h4>Description</h4><p>Ut ut tellus augue, ut rhoncus massa. Donec nisl nulla, molestie a semper in, luctus ac nunc. Cras eget nibh eu eros sollicitudin imperdiet.</p><div class="btn">view</div></div>
  <div class="abs feature" style="left:404px;top:552px"><svg class="feature-icon" viewBox="0 0 48 50"><use href="#magnifier"/></svg><h4>Description</h4><p>Ut ut tellus augue, ut rhoncus massa. Donec nisl nulla, molestie a semper in, luctus ac nunc. Cras eget nibh eu eros sollicitudin imperdiet.</p><div class="btn">view</div></div>
  <div class="abs feature" style="left:572px;top:552px"><svg class="feature-icon" viewBox="0 0 48 50"><use href="#magnifier"/></svg><h4>Description</h4><p>Ut ut tellus augue, ut rhoncus massa. Donec nisl nulla, molestie a semper in, luctus ac nunc. Cras eget nibh eu eros sollicitudin imperdiet.</p><div class="btn">view</div></div>
  <div class="abs feature" style="left:236px;top:692px"><svg class="feature-icon" viewBox="0 0 48 50"><use href="#magnifier"/></svg><h4>Description</h4><p>Ut ut tellus augue, ut rhoncus massa. Donec nisl nulla, molestie a semper in, luctus ac nunc. Cras eget nibh eu eros sollicitudin imperdiet.</p><div class="btn">view</div></div>
  <div class="abs feature" style="left:404px;top:692px"><svg class="feature-icon" viewBox="0 0 48 50"><use href="#magnifier"/></svg><h4>Description</h4><p>Ut ut tellus augue, ut rhoncus massa. Donec nisl nulla, molestie a semper in, luctus ac nunc. Cras eget nibh eu eros sollicitudin imperdiet.</p><div class="btn">view</div></div>
  <div class="abs feature" style="left:572px;top:692px"><svg class="feature-icon" viewBox="0 0 48 50"><use href="#magnifier"/></svg><h4>Description</h4><p>Ut ut tellus augue, ut rhoncus massa. Donec nisl nulla, molestie a semper in, luctus ac nunc. Cras eget nibh eu eros sollicitudin imperdiet.</p><div class="btn">view</div></div>

  <div class="abs session">
    <h3>Title of the session</h3>
    <p>Sed semper sagittis ligula, ac convallis dolor lobortis vel. Aenean lacinia, sem non volutpat fermentum, sem enim venenatis turpis, vitae dapibus sem erat vehicula dolor. Donec eget felis ut lacus adipiscing sodales eget mattis lacus.</p>
    <div class="btn">read more</div>
  </div>

  <div class="abs shot" style="left:282px;top:840px"><div class="shot-img" role="img" aria-label="Gallery image placeholder"></div><div class="shot-cap">Description Image</div></div>
  <div class="abs shot" style="left:519px;top:840px"><div class="shot-img" role="img" aria-label="Gallery image placeholder"></div><div class="shot-cap">Description Image</div></div>
  <div class="abs shot" style="left:282px;top:997px"><div class="shot-img" role="img" aria-label="Gallery image placeholder"></div><div class="shot-cap">Description Image</div></div>
  <div class="abs shot" style="left:519px;top:997px"><div class="shot-img" role="img" aria-label="Gallery image placeholder"></div><div class="shot-cap">Description Image</div></div>

  <footer>
    <div class="abs foot-col" style="left:72px">
      <h5>Pages</h5>
      <ul class="pages"><li>Home</li><li>Services</li><li>Partners</li><li>About us</li><li>Contact</li></ul>
    </div>
    <div class="abs divider" style="left:206px"></div>
    <div class="abs foot-col" style="left:240px;width:110px">
      <h5>Last updates</h5>
      <ul class="bullets"><li>In hac habitasse platea dictumst. Praesent iaculis</li><li style="margin-top:6px">Faucibus pretium. Nullam dictum viverra augue id</li></ul>
    </div>
    <div class="abs divider" style="left:374px"></div>
    <div class="abs foot-col" style="left:409px;width:130px">
      <h5>Contact<br>information</h5>
      <p style="padding-left:8px;line-height:14px">Our telephones:<br>184460271<br>126730845<br>Our email:<br>example@example.com</p>
    </div>
    <div class="abs divider" style="left:542px"></div>
    <div class="abs foot-col" style="left:578px;width:120px">
      <h5>Our affiliates</h5>
      <ul class="bullets"><li>Lorem ipsum dolor</li><li>Egestas diam</li><li>Aliquet Hendrerit</li><li>Libero et sudis</li><li>Non potest augue</li><li>Vehicula tempus porta</li></ul>
    </div>
    <div class="abs foot-brand"><strong>Brambleview Telco</strong><span>all rights reserved.</span></div>
  </footer>
</div>
</body>
</html>
```